Flyer für Beratung, Planung und Montage von Photovoltaikanlagen, Wallboxen usw.
Der Ablauf war optimal. Auf Änderungswünsche wurde umgehend eingegangen. Die Bearbeitung erfolgt sehr zeitnah. Wir sind sehr zufrieden und können TOLVERIKO nur empfehlen.
Zielgruppe
Individuelle Beratung, Planung und Montage von Photovoltaikanlagen, Wallboxen, Balkonkraftwerke, PowerToHeat, Stromspeicher etc., (Neuanlagen & Bestandsanlagen), Privat- & Firmenkunden
Aufgabenstellung
Qualitativ hochwertige Markenprodukte, Seriös, Modern, Regionaler Anbieter, Flyer für gezielte regionale Verteilung (Briefkasten)

```html
<!DOCTYPE html>
<html lang="de">
<head>
<meta charset="utf-8">
<title>Flusstal Energie – Flyer</title>
<link href="https://fonts.googleapis.com/css2?family=Krona+One&family=Poppins:wght@300;400;500;600;700&display=swap" rel="stylesheet">
<style>
  :root{
    --stage:#7d9897;
    --dark:#323b39;
    --lime:#b5cc18;
    --lime-light:#d3e36a;
    --paper:#f1f1f0;
    --grey:#dcdcdc;
    --ink:#1b1f1e;
    --ink-soft:#3a403e;
    --white:#ffffff;
  }
  *{box-sizing:border-box;margin:0;padding:0}
  html,body{width:1200px;height:1117px;overflow:hidden}
  body{background:var(--stage);font-family:"Poppins",sans-serif;position:relative}
  .flyer{position:absolute;left:220px;top:20px;width:760px;height:1077px;background:var(--paper);overflow:hidden;box-shadow:0 10px 30px rgba(0,0,0,.25)}
  .hero{position:absolute;left:0;top:0;width:760px;height:490px;
    background:linear-gradient(180deg,#4b5479 0%,#6b7190 30%,#5a5f6a 55%,#3f4a2e 80%,#4f6b2a 100%)}
  .hero-glow{position:absolute;left:0;top:0;width:100%;height:100%;
    background:radial-gradient(ellipse at 45% 70%,rgba(230,160,70,.35),transparent 55%)}
  .welcome{position:absolute;left:330px;top:64px;color:var(--white);font-weight:600;font-size:17px}
  .brand{position:absolute;left:436px;top:145px;display:flex;align-items:center;gap:10px;color:var(--white);font-weight:400;font-size:24px;letter-spacing:3px}
  .brand-mark{width:14px;height:14px;background:var(--white)}
  .stripe{position:absolute;left:0;top:440px;width:760px;height:60px}
  .intro{position:absolute;left:0;top:470px;width:760px;height:250px;background:var(--dark);text-align:center;color:var(--white)}
  .headline{font-family:"Krona One",sans-serif;font-size:27px;line-height:36px;margin-top:38px}
  .headline .accent{color:var(--lime);display:block}
  .lead{font-weight:300;font-size:12.6px;line-height:17px;width:620px;margin:14px auto 0}
  .services-tab{position:absolute;left:238px;top:697px;width:284px;height:42px;background:var(--dark);border:2px solid var(--white);border-radius:12px;transform:skewX(-10deg);}
  .services-tab span{display:block;transform:skewX(10deg);text-align:center;line-height:38px;color:var(--white);font-weight:600;font-size:19px}
  .services-tab em{font-style:normal;color:var(--lime)}
  .services{position:absolute;left:59px;top:760px;display:flex;gap:12px}
  .service{width:152px}
  .service-photo{width:152px;height:100px}
  .service h3{font-weight:600;font-size:13.5px;line-height:15.5px;color:var(--ink-soft);margin-top:12px}
  .service p{font-size:8.3px;line-height:10px;color:var(--ink);margin-top:6px}
  .photo-pv{background:linear-gradient(180deg,#e8a54a 0%,#b77a3a 40%,#3a3f45 100%)}
  .photo-storage{background:linear-gradient(90deg,#f4f4f4 0%,#d8d8d8 40%,#2a2a2a 70%,#f4f4f4 100%)}
  .photo-service{background:linear-gradient(180deg,#d7dde3 0%,#c9ccc9 60%,#5b6b7a 100%)}
  .photo-charging{background:linear-gradient(90deg,#8e7b5c 0%,#c7c4b8 50%,#eeeeee 100%)}
  .footer{position:absolute;left:0;top:945px;width:760px;height:132px;background:var(--grey);clip-path:polygon(0 0,100% 25px,100% 100%,0 100%)}
  .cta{position:absolute;left:67px;top:987px;font-size:13.5px;line-height:17px;color:var(--ink)}
  .cta strong{font-weight:600}
  .phone-icon{display:inline-block;vertical-align:-2px;margin-left:6px}
  .closing{position:absolute;left:67px;top:1025px;font-weight:700;font-size:19px;color:var(--ink)}
  .web{position:absolute;left:435px;top:1030px;width:325px;height:47px;background:var(--lime);border-top-left-radius:30px;clip-path:polygon(14px 0,100% 0,100% 100%,0 100%);color:var(--dark);font-weight:700;font-size:19px;line-height:47px;text-align:right;padding-right:48px}
</style>
</head>
<body>
<main class="flyer">
  <div class="hero" role="img" aria-label="Foto: modernes Einfamilienhaus mit Solaranlage auf dem Dach in der Abenddämmerung">
    <div class="hero-glow"></div>
  </div>
  <p class="welcome">Willkommen bei</p>
  <div class="brand"><span class="brand-mark"></span>FLUSSTAL ENERGIE</div>

  <svg class="stripe" viewBox="0 0 760 60" preserveAspectRatio="none" aria-hidden="true">
    <polygon points="0,22 760,2 760,14 0,36" fill="var(--lime-light)"/>
    <polygon points="0,36 760,14 760,26 0,48" fill="var(--lime)"/>
  </svg>

  <section class="intro">
    <h1 class="headline">Ihr regionaler Anbieter für<span class="accent">erneuerbare Energien</span></h1>
    <p class="lead">Wir sind Ihre regionalen Experten für maßgeschneiderte Photovoltaik- und Stromspeicherlösungen. Egal, ob Sie Privat- oder Gewerbekunde sind. Wir bieten passgenaue Lösungen und 360° Service für Ihre individuellen Bedürfnisse – und das sowohl für Neu- als auch Bestandsanlagen. Von der detaillierten Planung bis zur professionellen Installation und darüber hinaus.</p>
  </section>

  <div class="services-tab"><span>Unsere <em>Leistungen:</em></span></div>

  <section class="services">
    <article class="service">
      <div class="service-photo photo-pv" role="img" aria-label="Foto: Gewerbehalle mit Solardach bei Sonnenuntergang"></div>
      <h3>Sistem fotovoltaik</h3>
      <p><strong>360° Service rund um ihre PV-Anlage</strong></p>
    </article>
    <article class="service">
      <div class="service-photo photo-storage" role="img" aria-label="Foto: Stromspeicher-Geräte"></div>
      <h3>Stromspeicher</h3>
      <p>Privat- oder Gewerbespeicher für alle Bedürfnisse</p>
    </article>
    <article class="service">
      <div class="service-photo photo-service" role="img" aria-label="Foto: Holzwürfel mit Symbolen auf Solarmodul"></div>
      <h3>Wartung - Service und Monitoring</h3>
      <p>Wir informieren Sie sofort, wenn mit ihrer Anlage etwas nicht stimmt.</p>
    </article>
    <article class="service">
      <div class="service-photo photo-charging" role="img" aria-label="Foto: Elektroauto an Ladesäule vor Wohnhaus"></div>
      <h3>Ladeinfrastruktur und Elektromobilität</h3>
      <p>Ladeinfrastruktur und Elektromobilität</p>
    </article>
  </section>

  <div class="footer"></div>
  <p class="cta">Starten Sie jetzt Ihre ganz persönliche Energiewende und vereinbaren Sie noch<br>heute einen kostenfreien-Beratungstermin unter
    <svg class="phone-icon" width="13" height="13" viewBox="0 0 24 24" aria-hidden="true"><circle cx="12" cy="12" r="10.5" fill="none" stroke="var(--ink)" stroke-width="2"/><path d="M8.5 7c1 0 1.5 2 1.5 2.5s-1 1-1 1.5 2.5 3.5 3.5 3.5c.5 0 1-1 1.5-1s2.5.5 2.5 1.5-1 2-2 2C11 17.5 6.5 13 6.5 9c0-1 1-2 2-2z" fill="var(--ink)"/></svg>
    <strong>08145 – 3327180</strong></p>
  <p class="closing">Wir freuen uns auf Ihren Anruf!</p>
  <div class="web">www.flusstal-energie.de</div>
</main>
</body>
</html>
```